Luxury Bath Flyer

I would like to have a professional Flyer, which would describe a beautiful atmospheric luxury-Bath situation. I am sending you a( screenshot) Flyer Proposal, which shoes my intention and wish how I would like to have it. Please note that Ästhetik and a professional Flyer is very important to me. If possible send a psd.file or a indesign file, in case of we gonna need to change the text. You are also free to make 2 different proposals and one as you would suggest.?(I send you couple pictures, but the main one which I choose on the pdf file, please keep that, it is called " KR-71" - If there is a question please let me know. Looking forward to receive an amazing artwork.Kind Regards Merle
Look and feel
Each slider illustrates characteristics of the customer's brand and the style your logo design should communicate.

```html
<!DOCTYPE html>
<html lang="de">
<head>
<meta charset="utf-8">
<title>Wohnquelle – Ihr exklusives Bad zum Fixpreis</title>
<link rel="stylesheet" href="https://fonts.googleapis.com/css2?family=Montserrat:ital,wght@0,400;0,500;0,600;0,700;1,700;1,800&display=swap">
<style>
  :root{
    --navy:#1f3a52;
    --blue:#2aa3dc;
    --orange:#f5a623;
    --panel-dark:#2e2e30;
    --panel-mid:#3b3b3d;
    --page:#ebe8e4;
    --white:#ffffff;
    --ink:#1f3a52;
  }
  *{margin:0;padding:0;box-sizing:border-box}
  html,body{width:1200px;height:800px;overflow:hidden}
  body{background:var(--page);font-family:"Montserrat",sans-serif;position:relative}
  .flyer{position:absolute;left:328px;top:15px;width:545px;height:770px;background:var(--white);overflow:hidden}
  .flyer-art{position:absolute;inset:0}
  .headline{position:absolute;right:28px;top:32px;text-align:right;font-style:italic;font-weight:700;line-height:1.1}
  .headline-top{color:var(--white);font-size:20px;display:block}
  .headline-price{color:var(--orange);font-size:34px;font-weight:800;display:block;margin-top:6px}
  .claim{position:absolute;left:270px;top:394px;color:var(--ink);font-size:16px;font-weight:500;line-height:1.3}
  .claim strong{font-weight:700}
  .services-title{position:absolute;left:27px;top:463px;color:var(--ink);font-size:15px;font-weight:700}
  .services{position:absolute;left:27px;top:487px;width:230px;list-style:none}
  .service{height:40.5px;display:flex;align-items:center;gap:10px;padding:0 10px;color:var(--white);font-size:11px;line-height:1.2}
  .service:nth-child(odd){background:var(--panel-mid)}
  .service:nth-child(even){background:var(--panel-dark)}
  .service svg{flex:none}
  .benefits{position:absolute;left:280px;top:507px;color:var(--ink)}
  .benefits-title{color:var(--blue);font-size:15px;font-weight:700;margin-bottom:3px}
  .benefits ul{list-style:none;font-size:13px;font-weight:500;line-height:1.4}
  .benefits li::before{content:"• "}
  .hotline{position:absolute;left:0;top:673px;width:410px;height:51px;background:var(--blue);display:flex;align-items:center}
  .hotline svg{margin-left:22px}
  .hotline-number{color:var(--white);font-size:33px;font-weight:700;margin-left:14px;letter-spacing:.5px}
  .brand{position:absolute;left:402px;top:640px;width:127px;height:100px;background:var(--white);display:flex;align-items:center;justify-content:center;gap:6px;z-index:2}
  .brand-mark{width:10px;height:10px;background:var(--blue);flex:none}
  .brand-name{color:var(--ink);font-size:15px;font-weight:700}
  .contact-line{position:absolute;left:0;right:0;top:738px;text-align:center;color:var(--ink);font-size:10.5px;font-weight:500}
</style>
</head>
<body>
<main class="flyer">
  <svg class="flyer-art" width="545" height="770" viewBox="0 0 545 770">
    <defs>
      <linearGradient id="bath-tone" x1="0" y1="0" x2="0.4" y2="1">
        <stop offset="0" stop-color="#cfc8bf"/>
        <stop offset="0.35" stop-color="#e2ddd6"/>
        <stop offset="0.6" stop-color="#eeece9"/>
        <stop offset="1" stop-color="#fbfbfa"/>
      </linearGradient>
      <radialGradient id="bath-glow" cx="0.75" cy="0.35" r="0.5">
        <stop offset="0" stop-color="#ffffff" stop-opacity="0.7"/>
        <stop offset="1" stop-color="#ffffff" stop-opacity="0"/>
      </radialGradient>
      <linearGradient id="tile-tone" x1="0" y1="0" x2="1" y2="1">
        <stop offset="0" stop-color="#c9b29c"/>
        <stop offset="0.5" stop-color="#e7ddd2"/>
        <stop offset="1" stop-color="#f7f5f2"/>
      </linearGradient>
      <linearGradient id="tile-close" x1="0" y1="0" x2="1" y2="1">
        <stop offset="0" stop-color="#d7a98a"/>
        <stop offset="1" stop-color="#ecd8c6"/>
      </linearGradient>
    </defs>
    <rect width="545" height="770" fill="url(#bath-tone)" role="img" aria-label="Helles Badezimmer mit Waschtisch, Mosaikfliesen und Tulpen"/>
    <rect width="545" height="770" fill="url(#bath-glow)"/>
    <polygon points="0,0 545,0 545,92 195,442 0,215" fill="var(--navy)"/>
    <rect x="57" y="105" width="280" height="280" rx="36" transform="rotate(45 197 245)" fill="url(#tile-tone)" stroke="var(--blue)" stroke-width="12" role="img" aria-label="Waschtisch mit Armatur vor Mosaikfliesen und Tulpen"/>
    <rect x="245.5" y="144.5" width="175" height="175" rx="28" transform="rotate(45 333 232)" fill="var(--orange)"/>
    <rect x="232.5" y="167.5" width="135" height="135" rx="20" transform="rotate(45 300 235)" fill="url(#tile-close)" stroke="var(--white)" stroke-width="3" role="img" aria-label="Nahaufnahme Armatur vor Mosaikfliesen"/>
  </svg>

  <h1 class="headline">
    <span class="headline-top">Ihr exklusives Bad zum</span>
    <span class="headline-price">Fixpreis!</span>
  </h1>

  <p class="claim">Wir montieren für Sie...<br>und das <strong>„Alles aus einer Hand“</strong>!</p>

  <h2 class="services-title">Unsere Services</h2>
  <ul class="services">
    <li class="service"><svg width="16" height="20" viewBox="0 0 16 20"><polygon points="16,0 16,20 0,10" fill="var(--blue)"/></svg>Markenbäder zum Online Preis</li>
    <li class="service"><svg width="16" height="20" viewBox="0 0 16 20"><polygon points="16,0 16,20 0,10" fill="var(--blue)"/></svg>Wir montieren für Sie</li>
    <li class="service"><svg width="16" height="20" viewBox="0 0 16 20"><polygon points="16,0 16,20 0,10" fill="var(--blue)"/></svg>Funktionalität und Ästhetik</li>
    <li class="service"><svg width="16" height="20" viewBox="0 0 16 20"><polygon points="16,0 16,20 0,10" fill="var(--blue)"/></svg>Komplettlösungen mit rasche Umsetzung</li>
  </ul>

  <section class="benefits">
    <h3 class="benefits-title">Ihre Vorteile</h3>
    <ul>
      <li>Individuelle Badplanung</li>
      <li>Eigene Handwerker vor Ort</li>
      <li>Traumbad erlebniss</li>
    </ul>
  </section>

  <div class="hotline">
    <svg width="30" height="38" viewBox="0 0 24 30" aria-hidden="true"><path d="M6 1 L10 8 L7 11 C8 16 11 20 15 23 L18 20 L23 25 L19 29 C9 27 1 16 2 5 Z" fill="var(--navy)"/></svg>
    <span class="hotline-number">0800 314 926</span>
  </div>

  <div class="brand">
    <span class="brand-mark"></span>
    <span class="brand-name">Wohnquelle</span>
  </div>

  <p class="contact-line">Lindenweg 12, 2351 Ahornfeld | www.wohnquelle-bad.at | office@wohnquelle-bad.at</p>
</main>
</body>
</html>
```